Fieldstone Sporting
F.S.S. Sports
Project: Fieldstone Sporting
Fieldstone Sporting - Sports
Creative Brief
Use same font as used in my logo
Use your better judgement
Professional
Weston L. Barrow Jr.
CEO
Owings Mills, MD
W.barrow17@quillmail.example
www.FSSsports.example
Logo and web address
Concepts
Business card and stationary design. We provide umpires & referees for teams/organizations.

```html
<!DOCTYPE html>
<html lang="en">
<head>
<meta charset="utf-8">
<title>Fieldstone Sporting – Business Card</title>
<link href="https://fonts.googleapis.com/css2?family=Crimson+Text:ital,wght@0,400;0,700;1,700&display=swap" rel="stylesheet">
<style>
  :root {
    --backdrop: #e9eaec;
    --card: #ffffff;
    --navy: #2e4a9a;
    --green: #8cc63f;
    --green-text: #7aa82f;
    --ink: #3b3b3b;
    --rule: #b9bcc2;
  }
  * { box-sizing: border-box; margin: 0; padding: 0; }
  html, body {
    width: 1200px; height: 780px; overflow: hidden;
    background: var(--backdrop);
    font-family: "Crimson Text", Georgia, serif;
  }
  .canvas {
    position: relative; width: 1200px; height: 780px;
    display: flex; align-items: center; justify-content: center;
  }
  .business-card {
    position: relative; width: 1050px; height: 600px;
    background: var(--card); border-radius: 34px; overflow: hidden;
    box-shadow: 0 10px 30px rgba(0,0,0,.18);
  }
  .card-waves { position: absolute; inset: 0; width: 100%; height: 100%; }
  .brand {
    position: absolute; top: 100px; left: 0; width: 100%;
    display: flex; align-items: center; justify-content: center; gap: 22px;
  }
  .brand-dot { width: 34px; height: 34px; border-radius: 50%; background: var(--green); }
  .brand-name {
    font-weight: 700; font-size: 66px; color: var(--navy);
    letter-spacing: 1px; line-height: 1;
  }
  .identity { position: absolute; left: 140px; top: 272px; text-align: right; width: 360px; }
  .person-name { font-style: italic; font-weight: 700; font-size: 40px; color: var(--navy); line-height: 1.1; }
  .person-title { font-weight: 700; font-size: 24px; color: var(--green-text); margin-top: 2px; }
  .postal { font-size: 26px; color: var(--ink); margin-top: 30px; }
  .divider { position: absolute; left: 532px; top: 252px; width: 2px; height: 170px; background: var(--rule); }
  .contacts { position: absolute; left: 566px; top: 252px; list-style: none; }
  .contacts li {
    display: flex; align-items: center; gap: 14px;
    font-size: 27px; color: var(--ink); height: 42px;
  }
  .contacts svg { width: 24px; height: 24px; fill: var(--navy); flex: none; }
</style>
</head>
<body>
<main class="canvas">
  <article class="business-card">
    <svg class="card-waves" viewBox="0 0 1050 600" preserveAspectRatio="none" aria-hidden="true">
      <path d="M0 525 C 320 520, 720 495, 1050 450 L1050 600 L0 600 Z" fill="var(--green)"/>
      <path d="M0 539 C 320 534, 720 510, 1050 465 L1050 600 L0 600 Z" fill="#ffffff"/>
      <path d="M0 556 C 340 551, 740 527, 1050 482 L1050 600 L0 600 Z" fill="var(--navy)"/>
    </svg>

    <header class="brand">
      <span class="brand-dot"></span>
      <h1 class="brand-name">Fieldstone Sporting</h1>
    </header>

    <section class="identity">
      <p class="person-name">Weston L. Barrow Jr.</p>
      <p class="person-title">CEO</p>
      <p class="postal">P.O. Box Glenmoor, MD</p>
    </section>

    <div class="divider"></div>

    <ul class="contacts">
      <li>
        <svg viewBox="0 0 24 24"><path d="M6.6 10.8a15.1 15.1 0 0 0 6.6 6.6l2.2-2.2a1 1 0 0 1 1-.25 11.4 11.4 0 0 0 3.6.57 1 1 0 0 1 1 1V20a1 1 0 0 1-1 1A17 17 0 0 1 3 4a1 1 0 0 1 1-1h3.5a1 1 0 0 1 1 1c0 1.25.2 2.450.57 3.57a1 1 0 0 1-.25 1z"/></svg>
        410-555-0172
      </li>
      <li>
        <svg viewBox="0 0 24 24"><path d="M8 1h8a2 2 0 0 1 2 2v18a2 2 0 0 1-2 2H8a2 2 0 0 1-2-2V3a2 2 0 0 1 2-2zm0 3v14h8V4zm4 15.5a1.2 1.2 0 1 0 0 2.4 1.2 1.2 0 0 0 0-2.4z"/></svg>
        410-555-0148
      </li>
      <li>
        <svg viewBox="0 0 24 24"><path d="M7 2h10v5H7zM4 8h16a2 2 0 0 1 2 2v7h-4v5H6v-5H2v-7a2 2 0 0 1 2-2zm4 8v4h8v-4z"/></svg>
        410-555-0193
      </li>
      <li>
        <svg viewBox="0 0 24 24"><path d="M12 2a10 10 0 1 0 5 18.7l-1-1.7A8 8 0 1 1 20 12v1.2a1.8 1.8 0 0 1-3.6 0V7.5h-2v.9A5 5 0 1 0 15 16a3.8 3.8 0 0 0 7-2.8V12A10 10 0 0 0 12 2zm0 13a3 3 0 1 1 0-6 3 3 0 0 1 0 6z"/></svg>
        W.barrow17@quillmail.example
      </li>
    </ul>
  </article>
</main>
</body>
</html>
```